Commercial and Multifamily informational website

We need a website for our commercial real estate management company. We will manage offices, retail, apartments and others. Here is the brief verbiage: Providing quality commercial and multifamily portfolio management to Landlords, REITs, and financial institutions. 

Industry/Entity Type

Real Estate

Number of Pages Required

2 page

Font styles to use
Sans Serif
Other font styles liked:
• Muli, Garamond

Colors
0555a3
5c5c5c
3176b5
85acd3
474747

Requirements
Must have
• Home page and contact page

```html
<!DOCTYPE html>
<html lang="en">
<head>
<meta charset="utf-8">
<title>Kestrel Real Estate Management</title>
<link href="https://fonts.googleapis.com/css2?family=Mulish:wght@400;600;700;800&family=Montserrat:wght@300;400;500;600;700&display=swap" rel="stylesheet">
<style>
:root{
  --blue:#0555a3;
  --blue-deep:#1f4a8a;
  --blue-mid:#3176b5;
  --blue-soft:#85acd3;
  --grey:#5c5c5c;
  --grey-dark:#474747;
  --light:#f3f3f3;
  --footer:#3a3a3a;
  --footer-bottom:#2c2c2c;
  --white:#ffffff;
}
*{box-sizing:border-box;margin:0;padding:0}
html,body{width:1200px;height:3876px;overflow:hidden}
body{font-family:"Mulish",sans-serif;color:var(--grey);background:var(--white);position:relative}
h1,h2,h3{font-family:"Montserrat",sans-serif}
.btn{display:inline-block;font-family:"Mulish",sans-serif;font-weight:700;font-size:13px;color:var(--white);background:var(--blue-deep);padding:8px 18px;border-radius:2px;white-space:nowrap}
.btn-outline{background:var(--white);color:var(--grey-dark);border:1px solid #bbb}
.lorem{font-size:13px;line-height:1.7;color:#777}

/* header */
.site-header{position:absolute;top:0;left:0;width:1200px;height:120px;border-bottom:1px solid #e2e2e2}
.header-logo{position:absolute;left:150px;top:14px;width:90px;height:86px;background:var(--blue);display:flex;align-items:center;justify-content:center;color:var(--white);font-family:"Montserrat",sans-serif;font-weight:700;font-size:17px;letter-spacing:1px}
.top-info{position:absolute;top:14px;left:380px;right:150px;display:flex;justify-content:space-between;font-size:11px;color:var(--grey)}
.top-info span{display:flex;align-items:center;gap:6px;white-space:nowrap}
.main-nav{position:absolute;left:322px;right:150px;top:56px;display:flex;align-items:center;gap:15px;font-family:"Montserrat",sans-serif;font-size:11px;font-weight:600;color:var(--grey-dark);text-transform:uppercase;white-space:nowrap}
.main-nav .active{color:var(--blue)}
.main-nav .nav-cta{margin-left:auto;background:var(--blue-deep);color:var(--white);padding:8px 12px}
.header-rule{position:absolute;left:322px;right:150px;top:96px;height:3px;background:var(--blue)}

/* hero */
.hero{position:absolute;top:120px;left:0;width:1200px;height:420px}
.hero-title{position:absolute;left:140px;top:40px;width:520px}
.hero-title h1{font-size:32px;font-weight:700;color:var(--blue-deep);letter-spacing:1px;line-height:1;white-space:nowrap}
.hero-title p{font-family:"Montserrat",sans-serif;font-size:16px;color:var(--blue-mid);letter-spacing:1px;margin-top:6px;text-transform:uppercase}
.hero-photo{position:absolute;left:140px;top:120px;width:420px;height:300px;background:linear-gradient(135deg,#dbe7f2 0%,#a8bfd4 45%,#6f7d8c 100%);clip-path:polygon(0 20%,100% 0,100% 100%,0 100%)}
.request-box{position:absolute;left:688px;top:48px;width:392px;height:372px;background:var(--blue-deep);padding:36px 48px;color:var(--white)}
.request-box h3{font-size:24px;font-weight:500;text-align:center;margin-bottom:32px}
.request-box .field{height:30px;background:var(--white);margin-bottom:14px;font-size:11px;color:#999;padding:8px 10px}
.request-box .send{height:30px;background:var(--blue);text-align:center;font-weight:700;font-size:13px;padding-top:7px}

/* welcome */
.welcome{position:absolute;top:540px;left:0;width:1200px;height:290px;background:var(--light)}
.welcome-mark{position:absolute;left:170px;top:56px;width:370px;text-align:center}
.welcome-mark span{display:block;font-family:"Montserrat",sans-serif;font-size:24px;letter-spacing:6px;color:#8a8a8a;font-weight:500}
.welcome-mark strong{display:block;font-family:"Montserrat",sans-serif;font-size:62px;color:var(--blue);font-weight:700;line-height:1.1;letter-spacing:2px}
.welcome-copy{position:absolute;left:600px;top:50px;width:460px}
.welcome-copy .btn{margin-top:26px}

/* service cards */
.services{position:absolute;top:840px;left:140px;width:920px;height:272px;display:flex;gap:12px}
.service-card{flex:1;position:relative;background:linear-gradient(180deg,#4a78a6 0%,#2b5785 55%,#1f4a7a 100%);border:4px solid #d9e1ea;color:var(--white);text-align:center;padding:22px 18px}
.service-card h3{font-size:22px;font-weight:700;letter-spacing:1px;margin-bottom:14px}
.service-card p{font-size:14px;font-weight:700;line-height:1.35}
.service-card .btn{position:absolute;left:50%;transform:translateX(-50%);bottom:20px;font-size:11px;padding:5px 14px}

/* success stories */
.stories{position:absolute;top:1160px;left:0;width:1200px;height:460px;background:var(--light)}
.section-title{font-family:"Montserrat",sans-serif;font-size:34px;font-weight:400;color:var(--grey-dark);text-align:center;letter-spacing:1px}
.stories .section-title{position:absolute;top:26px;width:100%}
.story{position:absolute;top:140px;width:440px}
.story-photo{height:144px}
.story h3{font-family:"Mulish",sans-serif;font-size:16px;color:var(--grey-dark);font-weight:700;margin:14px 0 8px}
.story .btn{margin-top:12px;font-size:11px;padding:5px 12px}
.arrow{position:absolute;top:200px}

/* portal */
.portal{position:absolute;top:1660px;left:0;width:1200px;height:420px;background:linear-gradient(90deg,#d9dadb 0%,#e7e7e7 50%,#d4d4d4 100%)}
.portal .section-title{position:absolute;top:60px;width:100%;font-size:40px;color:#5e6b78}
.portal-rule{position:absolute;top:116px;left:140px;width:920px;height:1px;background:#9aa3ad}
.portal-intro{position:absolute;left:140px;top:150px;width:420px}
.portal-intro p.small{font-size:13px;color:#4b5a6a;line-height:1.6}
.portal-intro p.big{font-family:"Montserrat",sans-serif;font-size:26px;color:#2d3d52;margin-top:26px}
.portal-intro .btn{margin-top:22px;background:var(--blue-deep);font-size:16px;padding:10px 40px;display:flex;align-items:center;gap:10px;width:380px}
.portal-form{position:absolute;left:690px;top:150px;width:370px}
.portal-form label{display:block;font-size:12px;color:#4b5a6a;margin-bottom:6px}
.portal-form .field{height:36px;background:#ececec;border:1px solid #b9b9b9;margin-bottom:22px;font-size:11px;color:#999;padding:11px 10px}
.portal-form .login{height:38px;background:#6d6a62;color:var(--white);text-align:center;font-weight:700;padding-top:10px;font-size:14px}

/* about */
.about{position:absolute;top:2080px;left:0;width:1200px;height:480px;background:var(--white);overflow:hidden}
.about-photo{position:absolute;left:0;top:0;width:560px;height:480px;background:linear-gradient(180deg,#8a9bc1 0%,#c7b3bf 40%,#8b8d92 75%,#4d5a48 100%);clip-path:ellipse(555px 420px at 0 240px)}
.about-arc{position:absolute;left:0;top:0;width:570px;height:480px}
.about-copy{position:absolute;left:620px;top:40px;width:440px;text-align:center}
.about-copy h2{font-size:24px;font-weight:400;color:var(--blue-deep);line-height:1.3}
.about-divider{display:flex;align-items:center;gap:10px;justify-content:center;margin:18px 0}
.about-divider i{display:block;width:140px;height:1px;background:#999}
.about-divider b{width:8px;height:8px;border-radius:50%;border:1px solid #777}
.about-copy .lorem{font-size:12.5px;margin-bottom:14px}

/* testimonials */
.testimonials{position:absolute;top:2560px;left:0;width:1200px;height:560px;background:var(--blue-deep)}
.testimonials .section-title{position:absolute;top:28px;width:100%;color:var(--white);font-size:36px}
.testi-card{position:absolute;top:196px;width:308px;height:280px;background:var(--white);text-align:center;padding:86px 26px 0}
.avatar{position:absolute;left:50%;top:-56px;transform:translateX(-50%);width:112px;height:112px;border-radius:50%;background:linear-gradient(180deg,#7a5a4e,#c9a08a);border:6px solid #d8dfe8}
.testi-card h3{font-family:"Mulish",sans-serif;font-size:12px;color:var(--grey-dark);margin-bottom:10px}
.testi-card .lorem{font-size:11px;line-height:1.5}
.testi-card .btn{margin-top:14px;font-size:10px;padding:5px 12px}

/* contact */
.contact{position:absolute;top:3120px;left:0;width:1200px;height:400px;background:linear-gradient(135deg,#e9ebee 0%,#f3f4f5 50%,#e4e6e9 100%)}
.contact .section-title{position:absolute;top:60px;width:100%;font-size:34px}
.contact-rule{position:absolute;top:108px;left:140px;width:920px;height:1px;background:#999}
.contact-info{position:absolute;left:140px;top:130px;width:360px}
.contact-info h3{font-family:"Mulish",sans-serif;font-size:14px;color:var(--grey-dark);font-weight:600;margin-bottom:22px}
.info-row{display:flex;gap:14px;margin-bottom:18px;font-size:11px;line-height:1.5;color:var(--grey-dark)}
.contact-form{position:absolute;left:520px;top:130px;width:540px}
.contact-form h3{font-family:"Mulish",sans-serif;font-size:14px;color:var(--grey-dark);font-weight:600;margin-bottom:16px}
.contact-form .row{display:flex;gap:10px}
.contact-form .field{flex:1;height:32px;background:var(--white);border:1px solid #ccc;margin-bottom:10px;font-size:11px;color:#999;padding:9px 10px}
.contact-form .msg{height:80px}
.contact-form .send{width:90px;margin:6px auto 0;background:var(--blue-deep);color:var(--white);text-align:center;font-size:12px;font-weight:700;padding:7px 0}

/* footer */
.site-footer{position:absolute;top:3520px;left:0;width:1200px;height:320px;background:var(--footer);color:#ddd}
.footer-col{position:absolute;top:50px}
.footer-col h3{font-family:"Mulish",sans-serif;font-size:20px;font-weight:600;color:var(--white);margin-bottom:8px}
.footer-col hr{border:0;height:1px;background:#777;margin-bottom:18px}
.footer-links{display:grid;grid-template-columns:170px 140px;row-gap:12px;font-size:11px;text-transform:uppercase}
.footer-item{display:flex;gap:8px;font-size:11px;line-height:1.5;margin-bottom:16px}
.footer-col p{font-size:11px;line-height:1.6;text-transform:uppercase}
.footer-bottom{position:absolute;top:3840px;left:0;width:1200px;height:36px;background:var(--footer-bottom);color:#bbb;font-size:11px;padding:11px 110px;display:flex;justify-content:space-between;align-items:center}
.social{display:flex;gap:6px}
.social i{display:block;width:18px;height:18px;background:#777}
</style>
</head>
<body>

<header class="site-header">
  <div class="header-logo">KESTREL</div>
  <div class="top-info">
    <span><svg width="12" height="12" viewBox="0 0 12 12"><circle cx="6" cy="6" r="5" fill="none" stroke="#0555a3" stroke-width="1.4"/><path d="M6 3v3l2 1.5" stroke="#0555a3" stroke-width="1.2" fill="none"/></svg><b>Schedule</b> Monday to Saturday &nbsp; 8:00am to 6:00pm</span>
    <span><svg width="12" height="10" viewBox="0 0 12 10"><rect x="0.5" y="0.5" width="11" height="9" fill="none" stroke="#0555a3"/><path d="M0.5 0.5l5.5 5 5.5-5" fill="none" stroke="#0555a3"/></svg>info@kestrelre.com &nbsp;&nbsp;
    <svg width="12" height="12" viewBox="0 0 12 12"><path d="M2 1l2.5 0 1 3-1.5 1a7 7 0 0 0 3 3l1-1.5 3 1v2.5c0 .5-.5 1-1 1A10 10 0 0 1 1 2c0-.5.5-1 1-1z" fill="#0555a3"/></svg>(555) 014-2290</span>
  </div>
  <nav class="main-nav">
    <span class="active">Home</span><span>About</span><span>Properties</span><span>Promotions</span><span>Financing</span><span>Testimonial</span><span>Portal</span><span>Contact</span>
    <span class="nav-cta">Book Appointment</span>
  </nav>
  <div class="header-rule"></div>
</header>

<section class="hero">
  <div class="hero-title">
    <h1>PORTFOLIO MANAGEMENT</h1>
    <p>Done better than ever before</p>
  </div>
  <div class="hero-photo" role="img" aria-label="Photo of a modern glass office building seen from below"></div>
  <div class="request-box">
    <h3>Request a Consultant</h3>
    <div class="field">Name</div>
    <div class="field">Email</div>
    <div class="field">Phone</div>
    <div class="send">SEND</div>
  </div>
</section>

<section class="welcome">
  <div class="welcome-mark">
    <span>WELCOME TO</span>
    <strong>KESTREL</strong>
  </div>
  <div class="welcome-copy">
    <p class="lorem">Providing quality commercial and multifamily portfolio management to landlords, REITs and financial institutions. We look after offices, retail centers, housing and apartment communities with care, clear reporting and a local team that knows every property it serves and every tenant it keeps.</p>
    <span class="btn btn-outline">READ MORE</span>
  </div>
</section>

<section class="services">
  <div class="service-card"><h3>OFFICES</h3><p>Lorem ipsum dolor sit amet, consectetur adipiscing</p><span class="btn">READ MORE</span></div>
  <div class="service-card"><h3>RETAIL</h3><p>Lorem ipsum dolor sit amet, consectetur adipiscing</p><span class="btn">READ MORE</span></div>
  <div class="service-card"><h3>HOUSING</h3><p>Lorem ipsum dolor sit amet, consectetur adipiscing</p><span class="btn">READ MORE</span></div>
  <div class="service-card"><h3>APPARTS</h3><p>Lorem ipsum dolor sit amet, consectetur adipiscing</p><span class="btn">READ MORE</span></div>
</section>

<section class="stories">
  <h2 class="section-title">SUCCESS STORIES</h2>
  <svg class="arrow" style="left:110px" width="14" height="24" viewBox="0 0 14 24"><path d="M12 2L2 12l10 10" stroke="#aaa" stroke-width="2" fill="none"/></svg>
  <svg class="arrow" style="left:1076px" width="14" height="24" viewBox="0 0 14 24"><path d="M2 2l10 10L2 22" stroke="#aaa" stroke-width="2" fill="none"/></svg>
  <article class="story" style="left:140px">
    <div class="story-photo" role="img" aria-label="Photo of a happy family relaxing outdoors" style="background:linear-gradient(180deg,#b9c7d6,#7b8c99 60%,#4f5c66)"></div>
    <h3>Lorem ipsum dolor sit amet, consectetur arcu</h3>
    <p class="lorem">Tenants moved into their new offices on schedule and the owners saw occupancy rise across the full portfolio within the first year of our care.</p>
    <span class="btn btn-outline">Read More</span>
  </article>
  <article class="story" style="left:620px">
    <div class="story-photo" role="img" aria-label="Photo of a woman with a hat by the sea" style="background:linear-gradient(180deg,#cfdbe6,#9fb5c8 55%,#5e7387)"></div>
    <h3>Lorem ipsum dolor sit amet, consectetur arcu</h3>
    <p class="lorem">A residential owner handed us three buildings and now enjoys steady income, fewer vacancies and clear monthly reports on every unit.</p>
    <span class="btn btn-outline">Read More</span>
  </article>
</section>

<section class="portal">
  <h2 class="section-title">PORTAL</h2>
  <div class="portal-rule"></div>
  <div class="portal-intro">
    <p class="small">Our secure Portal features a robust Electronic Workflow Records (EWR) system that keeps track of all aspects of your portfolio.</p>
    <p class="big">Lorem ipsum dolor sit amet.</p>
    <span class="btn"><svg width="16" height="16" viewBox="0 0 12 12"><path d="M2 1l2.5 0 1 3-1.5 1a7 7 0 0 0 3 3l1-1.5 3 1v2.5c0 .5-.5 1-1 1A10 10 0 0 1 1 2c0-.5.5-1 1-1z" fill="#fff"/></svg>Schedule a call now!</span>
  </div>
  <div class="portal-form">
    <label>Your Name</label>
    <div class="field">e.g. owner.name@example.com</div>
    <label>Your Password</label>
    <div class="field">••••••••</div>
    <div class="login">Login</div>
  </div>
</section>

<section class="about">
  <div class="about-photo" role="img" aria-label="Photo of a suburban family house at dusk"></div>
  <svg class="about-arc" viewBox="0 0 570 480"><ellipse cx="0" cy="240" rx="555" ry="420" fill="none" stroke="#1f4a8a" stroke-width="10"/></svg>
  <div class="about-copy">
    <h2>Welcome to Kestrel Real Estate Management, located in sunny Harbor Vale, CA.</h2>
    <div class="about-divider"><i></i><b></b><i></i></div>
    <p class="lorem">Lorem ipsum dolor sit amet, consectetur adipiscing elit. Vestibulum pulvinar blandit lorem et condimentum. Fusce eget pulvinar dolor. Mauris est ante, placerat et tortor id, tempus molestie ante. Proin porta tellus nec erat luctus, id consequat lorem condimentum.</p>
    <p class="lorem">Cras lorem lorem, commodo fermentum sagittis tempus quis, vulputate. Sed semper, arcu vel pharetra pellentesque, ex mi porta felis, vitae interdum magna augue sed. Ut faucibus tristique ipsum nec elementum, integer nec ante erat.</p>
    <p class="lorem">Lorem ipsum dolor sit amet, consectetur adipiscing elit. Vestibulum pulvinar blandit lorem et condimentum, fusce eget pulvinar dolor lorem.</p>
  </div>
</section>

<section class="testimonials">
  <h2 class="section-title">Testimonials</h2>
  <div class="testi-card" style="left:106px"><div class="avatar" role="img" aria-label="Client portrait"></div><h3>adipiscing elit. Vestibulum nec auctor.</h3><p class="lorem">Lorem ipsum dolor sit amet, consectetur adipiscing elit, sed do eiusmod tempor incididunt ut labore et dolore.</p><span class="btn">Read More</span></div>
  <div class="testi-card" style="left:446px"><div class="avatar" role="img" aria-label="Client portrait"></div><h3>adipiscing elit. Vestibulum nec auctor.</h3><p class="lorem">Lorem ipsum dolor sit amet, consectetur adipiscing elit, sed do eiusmod tempor incididunt ut labore et dolore.</p><span class="btn">Read More</span></div>
  <div class="testi-card" style="left:786px"><div class="avatar" role="img" aria-label="Client portrait"></div><h3>adipiscing elit. Vestibulum nec auctor.</h3><p class="lorem">Lorem ipsum dolor sit amet, consectetur adipiscing elit, sed do eiusmod tempor incididunt ut labore et dolore.</p><span class="btn">Read More</span></div>
</section>

<section class="contact" role="img" aria-label="Faded street map background">
  <h2 class="section-title">CONTACT US</h2>
  <div class="contact-rule"></div>
  <div class="contact-info">
    <h3>We are conveniently located at:</h3>
    <div class="info-row"><svg width="14" height="18" viewBox="0 0 14 18"><path d="M7 0a7 7 0 0 0-7 7c0 5 7 11 7 11s7-6 7-11a7 7 0 0 0-7-7z" fill="#474747"/><circle cx="7" cy="7" r="2.5" fill="#fff"/></svg><span>1450 ELM HARBOR RD, SUITE 3<br>HARBOR VALE, CA 90000</span></div>
    <div class="info-row"><svg width="14" height="14" viewBox="0 0 12 12"><path d="M2 1l2.5 0 1 3-1.5 1a7 7 0 0 0 3 3l1-1.5 3 1v2.5c0 .5-.5 1-1 1A10 10 0 0 1 1 2c0-.5.5-1 1-1z" fill="#474747"/></svg><span>(555) 014-2290<br>(555) 014-2291</span></div>
    <div class="info-row"><svg width="14" height="12" viewBox="0 0 12 10"><rect x="0.5" y="0.5" width="11" height="9" fill="none" stroke="#474747"/><path d="M0.5 0.5l5.5 5 5.5-5" fill="none" stroke="#474747"/></svg><span>info@kestrelre.com</span></div>
  </div>
  <div class="contact-form">
    <h3>Questions about options? Contact us.</h3>
    <div class="row"><div class="field">Name</div><div class="field">Email</div></div>
    <div class="field msg">Message</div>
    <div class="send">Send</div>
  </div>
</section>

<footer class="site-footer">
  <div class="footer-col" style="left:110px;width:330px">
    <h3>Quick Link</h3><hr>
    <div class="footer-links">
      <span>Home</span><span>Testimonials</span>
      <span>About</span><span>Portal</span>
      <span>Properties</span><span>Contact</span>
      <span>Promotions</span><span>Careers</span>
      <span>Financing</span><span>FAQ</span>
    </div>
  </div>
  <div class="footer-col" style="left:500px;width:300px">
    <h3>Contact Details</h3><hr>
    <div class="footer-item"><svg width="14" height="14" viewBox="0 0 14 14"><path d="M2 7l3 3 7-7" stroke="#ccc" stroke-width="2" fill="none"/></svg><span>Lorem ipsum dolor sit amet,<br>consectetur elit, sed do eiusmod</span></div>
    <div class="footer-item"><svg width="14" height="14" viewBox="0 0 14 14"><path d="M2 7l3 3 7-7" stroke="#ccc" stroke-width="2" fill="none"/></svg><span>Lorem ipsum dolor sit amet,<br>consectetur elit, sed do eiusmod</span></div>
  </div>
  <div class="footer-col" style="left:850px;width:240px">
    <h3>Contact Details</h3><hr>
    <p>1450 Elm Harbor Rd, Suite 3<br>Harbor Vale, CA 90000<br>(555) 014-2290<br>info@kestrelre.com</p>
  </div>
</footer>
<div class="footer-bottom">
  <span>©Kestrel. All Rights Reserved</span>
  <div class="social"><i></i><i></i><i></i><i></i></div>
</div>

</body>
</html>
```